5-star Hotel Web Design Project

I need a custom website design for a 5-star hotel. For full details please look at the attached ZIP archive.

The design should be in layers in Photoshop/Illustrator/InDesign format with all the icons/shapes/maps/graphic assets in vector format (svg, ai, eps) as much as possible.

I prefer white, simple but elegant websites. Please consider the performance/coding experience. We're not making something to show off our design skills on a design contest with fancy parallax effects and confusing animations. We're trying to create usable, functional and clean UI with good UX.

I would like to receive a few option for the color scheme to choose from.

The website will be custom coded, i.e. I'm not using WordPress.

NOTE: Don't bother to submit the generic WordPress style templates. We're looking for something custom made with attention to details. That's why the price is not guaranteed, but don't be mistaken, I'm a long time buyer here on SketchHive and all my projects are paid in full.

Low design quality

Europe

Hotel

5+ page

```html
<!DOCTYPE html>
<html lang="en">
<head>
<meta charset="utf-8">
<title>Coral Bay Resort</title>
<link href="https://fonts.googleapis.com/css2?family=Lora:ital,wght@0,400;0,600;1,400&family=Merriweather:wght@700&family=Arimo:wght@400&display=swap" rel="stylesheet">
<style>
:root{
  --crimson:#8c0a2e;
  --gold:#c99a4e;
  --gold-soft:#d3a85f;
  --ink:#333;
  --grey:#555;
  --line:#d8c7a8;
  --footer:#1e1e1e;
  --white:#fff;
}
*{margin:0;padding:0;box-sizing:border-box}
html,body{width:1200px;height:4988px;overflow:hidden}
body{position:relative;background:var(--white);font-family:"Lora",serif;color:var(--ink)}
.abs{position:absolute}
section,header,footer{position:absolute;left:0;width:1200px;overflow:hidden}
.sans{font-family:"Arimo",Arial,sans-serif}
.stars{color:var(--gold);font-size:13px;letter-spacing:2px;text-align:center}
.divider{position:absolute;left:50%;transform:translateX(-50%);width:220px;display:flex;align-items:center;gap:8px}
.divider::before,.divider::after{content:"";flex:1;height:1px;background:var(--gold)}
.section-title{position:absolute;left:0;width:1200px;text-align:center;font-size:37px;color:var(--crimson);font-weight:400}
.lead{position:absolute;left:0;width:1200px;text-align:center;font-family:"Arimo",Arial,sans-serif;font-size:14px;color:var(--grey)}
.pill{position:absolute;display:flex;align-items:center;justify-content:center;border-radius:30px;font-family:"Lora",serif;text-transform:uppercase;font-size:15px}
.pill-solid{background:var(--crimson);color:#fff}
.pill-line{border:1.5px solid var(--crimson);color:var(--crimson);background:#fff}

/* hero */
.hero{top:0;height:836px;background:linear-gradient(180deg,#2b2220 0%,#3b2d25 40%,#2a211c 75%,#1d1714 100%)}
.hero-photo{position:absolute;inset:0;background:radial-gradient(ellipse at 12% 30%,rgba(190,150,70,.45),transparent 25%),radial-gradient(ellipse at 75% 45%,rgba(120,90,60,.35),transparent 40%),linear-gradient(180deg,rgba(0,0,0,.35),rgba(0,0,0,.2))}
.brand{position:absolute;left:110px;top:40px;display:flex;align-items:center;gap:12px;color:var(--crimson);font-size:22px}
.brand-dot{width:40px;height:40px;border-radius:50%;border:2px solid var(--gold)}
.call{left:760px;top:50px;color:#fff;font-size:16px}
.contact{left:945px;top:40px;width:145px;height:45px;background:var(--gold);color:#fff;display:flex;align-items:center;justify-content:center;font-size:17px;border-radius:2px}
.nav{left:444px;top:116px;display:flex;gap:60px;color:#fff;font-size:17px}
.nav .lang{color:#ddd;font-size:14px}
.hero-title{top:352px;left:0;width:1200px;text-align:center;color:#fff;font-family:"Merriweather",serif;font-size:46px}
.hero-price{top:426px;left:0;width:1200px;text-align:center;color:var(--gold-soft);font-family:"Merriweather",serif;font-size:48px}
.field{top:532px;height:50px;background:#fff;display:flex;align-items:center;justify-content:space-between;padding:0 16px;font-size:16px;color:#444;border-radius:2px}
.check-btn{left:781px;top:532px;width:221px;height:50px;background:var(--crimson);color:#fff;display:flex;align-items:center;justify-content:center;font-size:17px;border-radius:2px}

/* glance */
.glance{top:836px;height:596px}
.badge{top:309px;width:233px;height:119px;border:1px solid #ccc;box-shadow:0 2px 5px rgba(0,0,0,.1);background:#fff;display:flex;align-items:center;justify-content:center}
.badge span{width:120px;height:40px;border-radius:20px;background:#e7e3dc}

/* offers */
.offers{top:1432px;height:933px;background:linear-gradient(180deg,#f0f0f0,#e9e9e9 50%,#f2f2f2)}
.offer{width:308px;height:271px;background:rgba(255,255,255,.8);border:1px solid #cfd9d6;box-shadow:0 1px 4px rgba(0,0,0,.08)}
.offer-frame{position:absolute;inset:13px;border:2px solid var(--gold);border-left-color:var(--crimson);border-bottom-color:var(--gold);background:linear-gradient(180deg,rgba(255,255,255,.95),rgba(232,244,232,.9));text-align:center}
.offer h3{margin-top:30px;font-size:18px;font-weight:400;color:var(--crimson);text-transform:uppercase}
.offer p{margin:14px auto 0;width:230px;font-style:italic;font-size:14px;line-height:25px;color:#555}
.price{color:var(--gold);font-size:33px;font-weight:600}
.price small{font-size:16px;font-weight:400}
.offer .price{margin-top:6px}
.offer .pill{left:78px;bottom:30px;width:124px;height:38px;font-size:13px;border-width:2px}

/* testimonials */
.testimonials{top:2365px;height:505px;background:linear-gradient(180deg,#c8974c,#c59449)}
.testi-title{left:112px;top:100px;color:#fff;font-size:44px;font-weight:400}
.testi-text{left:112px;top:172px;width:530px;color:#fff;font-size:14px;line-height:29px;text-align:justify}
.testi-name{left:112px;top:340px;color:#fff;font-size:20px}
.testi-date{left:112px;top:376px;color:#fff;font-size:14px}
.testi-photo{left:697px;top:60px;width:366px;height:366px;border-radius:50%;background:radial-gradient(circle at 50% 40%,#d9d6d2,#a9a7a4 60%,#6f6d6b)}

/* features */
.features{top:2870px;height:908px}
.feature{width:402px;height:164px;color:#fff}
.feature.crimson{background:var(--crimson)}
.feature.gold{background:var(--gold)}
.feature-badge{position:absolute;left:-58px;top:0;width:164px;height:164px;border-radius:50%;background:#fff;display:flex;align-items:center;justify-content:center}
.feature-badge svg{width:74px;height:74px}
.feature h4{position:absolute;left:100px;top:32px;font-size:19px;font-weight:400}
.feature h4::after{content:"";display:block;width:26px;height:2px;background:#fff;margin-top:12px}
.feature p{position:absolute;left:100px;top:82px;width:290px;font-size:13px;line-height:25px}

/* newsletter */
.newsletter{top:3778px;height:353px;background:var(--crimson)}
.newsletter .section-title{color:#fff}
.newsletter .lead{color:#fff}
.subscribe{left:176px;top:207px;width:848px;height:63px;border-radius:32px;background:#fff;overflow:hidden}
.subscribe .email{position:absolute;left:30px;top:20px;font-size:18px;color:#555}
.subscribe .go{position:absolute;right:0;top:0;width:176px;height:63px;background:var(--gold);color:#fff;display:flex;align-items:center;justify-content:center;font-size:18px}

/* accommodation */
.rooms{top:4131px;height:639px}
.room{top:192px;width:185px;height:374px;background:#fff;border:1px solid #eee;text-align:center}
.room.active{box-shadow:0 4px 16px rgba(140,10,46,.25)}
.room-photo{height:162px;background:linear-gradient(160deg,#6b3a22,#a46a3d 45%,#3c261a)}
.room-size{position:absolute;left:5px;top:25px;background:var(--crimson);color:#fff;font-size:13px;padding:5px 6px}
.room h5{margin-top:20px;font-size:21px;font-weight:400;color:#333}
.room p{margin:10px auto 0;width:160px;font-size:11px;line-height:20px;color:#555}
.room .price{font-size:24px;margin-top:4px}
.room .price small{font-size:15px}
.room .pill{left:38px;bottom:22px;width:110px;height:40px;text-transform:none;font-size:15px}

/* footer */
.site-footer{top:4770px;height:218px;background:var(--footer);color:#fff;font-size:16px}
.foot-links{left:135px;line-height:42px;top:42px}
.foot-sep{left:620px;top:44px;width:1px;height:130px;background:#444}
.foot-legal{left:690px;top:42px;line-height:42px}
.foot-legal .copy{font-size:14px}
</style>
</head>
<body>

<header class="hero">
  <div class="hero-photo" role="img" aria-label="Dimly lit luxury hotel suite interior with lamp, sofa and city windows"></div>
  <div class="brand"><span class="brand-dot"></span>Coral Bay Resort</div>
  <div class="abs call">Call Us : 000-555-0142</div>
  <div class="abs contact">Contact</div>
  <nav class="abs nav"><span>Coral Bay Resort</span><span>Book direct</span><span>Special Offers</span><span>Location &nbsp;| <span class="lang">EN ▾</span></span></nav>
  <h1 class="abs hero-title">Book direct with 20% discount</h1>
  <div class="abs hero-price">$55 Per Night</div>
  <div class="abs field" style="left:197px;width:281px">Check In
    <svg width="16" height="16" viewBox="0 0 16 16"><rect x="2" y="3" width="12" height="11" fill="none" stroke="#444" stroke-width="1.5"/><rect x="2" y="3" width="12" height="3" fill="#444"/></svg></div>
  <div class="abs field" style="left:489px;width:281px">Check Out
    <svg width="16" height="16" viewBox="0 0 16 16"><rect x="2" y="3" width="12" height="11" fill="none" stroke="#444" stroke-width="1.5"/><rect x="2" y="3" width="12" height="3" fill="#444"/></svg></div>
  <div class="abs check-btn">Check Availability</div>
</header>

<section class="glance">
  <h2 class="section-title" style="top:52px">At A Glance</h2>
  <div class="divider" style="top:102px"><span class="stars">★★★★★</span></div>
  <p class="lead" style="top:140px;left:230px;width:740px;line-height:30px">Sed ut perspiciatis unde omnis iste natus error sit voluptatem accusantium doloremque laudantium, totam rem aperiam, eaque ipsa quae ab illo inventore veritatis et quasi architecto beatae vitae dicta sunt explica bo. Nemo enim ipsam voluptatem quia voluptas sit aspernatur aut odit aut fugit, sed quia consequuntur magni dolores eos qui ratione voluptatem sequi nesciun</p>
  <div class="abs badge" style="left:199px"><span></span></div>
  <div class="abs badge" style="left:483px"><span></span></div>
  <div class="abs badge" style="left:767px"><span></span></div>
  <div class="pill pill-solid" style="left:500px;top:474px;width:200px;height:57px">Read More</div>
</section>

<section class="offers">
  <h2 class="section-title" style="top:50px">Special Offers</h2>
  <div class="divider" style="top:100px"><span class="stars">★★★★★</span></div>
  <p class="lead" style="top:146px">Sed ut perspiciatis unde omnis iste natus error sit voluptatem accusantium doloremque laudantium</p>

  <div class="abs offer" style="left:110px;top:215px"><div class="offer-frame"><h3>Easter Offer</h3><p>Sed ut perspiciatis unde omnis iste natus error sit</p><div class="price">$25<small>/Per Night</small></div><div class="pill pill-line">Book Now</div></div></div>
  <div class="abs offer" style="left:445px;top:215px"><div class="offer-frame"><h3>Summer Offer</h3><p>Sed ut perspiciatis unde omnis iste natus error sit</p><div class="price">$25<small>/Per Night</small></div><div class="pill pill-line">Book Now</div></div></div>
  <div class="abs offer" style="left:780px;top:215px"><div class="offer-frame"><h3>Early Bookings 2021</h3><p>Sed ut perspiciatis unde omnis iste natus error sit</p><div class="price">$25<small>/Per Night</small></div><div class="pill pill-line">Book Now</div></div></div>
  <div class="abs offer" style="left:110px;top:516px"><div class="offer-frame"><h3>New Year Offer</h3><p>Sed ut perspiciatis unde omnis iste natus error sit</p><div class="price">$25<small>/Per Night</small></div><div class="pill pill-line">Book Now</div></div></div>
  <div class="abs offer" style="left:445px;top:516px"><div class="offer-frame"><h3>Christmas Offer</h3><p>Sed ut perspiciatis unde omnis iste natus error sit</p><div class="price">$25<small>/Per Night</small></div><div class="pill pill-line">Book Now</div></div></div>
  <div class="abs offer" style="left:780px;top:516px"><div class="offer-frame"><h3>Special Offer -50%</h3><p>Sed ut perspiciatis unde omnis iste natus error sit</p><div class="price">$25<small>/Per Night</small></div><div class="pill pill-line">Book Now</div></div></div>

  <div class="pill pill-solid" style="left:500px;top:820px;width:200px;height:58px">View More</div>
</section>

<section class="testimonials">
  <h2 class="abs testi-title">Testimonials</h2>
  <p class="abs testi-text sans">Sed ut perspiciatis unde omnis iste natus error sit voluptatem accusantium dol oremque laudantium, totam rem aperiam, eaque ipsa quae ab illo inventore veritatis et quasi architecto beatae vitae dicta sunt explicabo. Nemo enim ipsam voluptatem quia voluptas sit aspernatur aut odit aut fugit, sed quia cons quuntur magni dolores eos qui ratione voluptatem sequi nesciunt.</p>
  <div class="abs testi-name">Marco Vell</div>
  <div class="abs testi-date">Posted on 20 Apr 2021</div>
  <div class="abs testi-photo" role="img" aria-label="Portrait photo of a smiling guest in a light shirt"></div>
</section>

<section class="features">
  <h2 class="section-title" style="top:46px">Features / Benefits</h2>
  <div class="divider" style="top:96px"><span class="stars">★★★★★</span></div>

  <div class="abs feature crimson" style="left:168px;top:166px">
    <div class="feature-badge"><svg viewBox="0 0 60 60" fill="none" stroke="#8c0a2e" stroke-width="2.5"><path d="M14 34a16 16 0 0 1 32 0"/><path d="M30 10v6M14 18l4 4M46 18l-4 4M8 34h6M46 34h6"/><path d="M10 42q5-4 10 0t10 0 10 0 10 0M10 50q5-4 10 0t10 0 10 0 10 0"/></svg></div>
    <h4>First line to the sea</h4><p class="sans">with direct access to the South beach in Lindhaven</p></div>
  <div class="abs feature gold" style="left:686px;top:166px">
    <div class="feature-badge"><svg viewBox="0 0 60 60" fill="none" stroke="#c99a4e" stroke-width="2.5"><path d="M12 52V14h10v38M12 24h10M12 34h10M22 22h18a8 8 0 0 1 0 16H28a6 6 0 0 0 0 12h20"/></svg></div>
    <h4>Aquapark</h4><p class="sans">32 fun water slides, 2 of which 150m long</p></div>

  <div class="abs feature gold" style="left:168px;top:368px">
    <div class="feature-badge"><svg viewBox="0 0 60 60" fill="none" stroke="#c99a4e" stroke-width="2.5"><rect x="12" y="10" width="36" height="28"/><path d="M18 32l8-10 6 7 4-4 6 7"/><path d="M10 52V42h40v10M14 42v-4h32v4"/></svg></div>
    <h4>Luxurious rooms</h4><p class="sans">Spacious open-air terraces and provide stunning views towards the Northern Bay as well as towards the enormous</p></div>
  <div class="abs feature crimson" style="left:686px;top:368px">
    <div class="feature-badge"><svg viewBox="0 0 60 60" fill="none" stroke="#8c0a2e" stroke-width="2.5"><path d="M16 8h6v10l4 8v26H12V26l4-8zM38 14h6v8l4 6v24H34V28l4-6z"/><path d="M12 34h14M34 36h14"/></svg></div>
    <h4>International restaurants &amp; bars</h4><p class="sans">4 international a-la-cart restaurants and 5 main buffet restaurants</p></div>

  <div class="abs feature crimson" style="left:168px;top:570px">
    <div class="feature-badge"><svg viewBox="0 0 60 60" fill="none" stroke="#8c0a2e" stroke-width="2.5"><circle cx="22" cy="14" r="5"/><path d="M20 20l-8 16h14l10-8M8 44h44M12 44v8M48 44v8M30 36h18"/></svg></div>
    <h4>Relax and Wellness center</h4><p class="sans">Plenty of options to boost your physical and mental energy and enhance your well-being</p></div>
  <div class="abs feature gold" style="left:686px;top:570px">
    <div class="feature-badge"><svg viewBox="0 0 60 60" fill="none" stroke="#c99a4e" stroke-width="2.5"><circle cx="26" cy="40" r="9"/><path d="M20 14h10l-4 26M30 40l14-22M40 12h10M14 52h28"/></svg></div>
    <h4>Fitness Center</h4><p class="sans">Enhance your physical condition!</p></div>

  <div class="pill pill-line" style="left:500px;top:790px;width:200px;height:57px;border-width:2px">View More</div>
</section>

<section class="newsletter">
  <h2 class="section-title" style="top:62px">Subscribe to Coral Bay Resort Newsletter</h2>
  <div class="divider" style="top:116px;width:220px"><span class="stars" style="color:#fff">★★★★★</span></div>
  <p class="lead" style="top:154px">Sed ut perspiciatis unde omnis iste natus error sit voluptatem accusantium doloremque laudantium</p>
  <div class="abs subscribe"><span class="email">Your Email</span><span class="go">Subscribe Me</span></div>
</section>

<section class="rooms">
  <h2 class="section-title" style="top:50px">Accommodation</h2>
  <div class="divider" style="top:100px"><span class="stars">★★★★★</span></div>
  <p class="lead" style="top:140px">Sed ut perspiciatis unde omnis iste natus error sit voluptatem accusantium doloremque laudantium</p>

  <div class="abs room" style="left:110px"><div class="room-photo" role="img" aria-label="Studio room with bed and wooden furniture"></div><span class="room-size">35 sq.m</span><h5>Studio</h5><p class="sans">Sed ut perspiciatis unde om natus error sit vol</p><div class="price">$25<small>/Per Night</small></div><div class="pill pill-line">View More</div></div>
  <div class="abs room" style="left:309px"><div class="room-photo" role="img" aria-label="Room A1 with dining table and chairs"></div><span class="room-size">35 sq.m</span><h5>A1</h5><p class="sans">Sed ut perspiciatis unde om natus error sit vol</p><div class="price">$25<small>/Per Night</small></div><div class="pill pill-line">View More</div></div>
  <div class="abs room active" style="left:508px"><div class="room-photo" role="img" aria-label="Room A2 living area with red sofa"></div><span class="room-size">35 sq.m</span><h5>A2</h5><p class="sans">Sed ut perspiciatis unde om natus error sit vol</p><div class="price">$25<small>/Per Night</small></div><div class="pill pill-solid" style="text-transform:none">View More</div></div>
  <div class="abs room" style="left:707px"><div class="room-photo" role="img" aria-label="Room A3 lounge with dining set"></div><span class="room-size">35 sq.m</span><h5>A3</h5><p class="sans">Sed ut perspiciatis unde om natus error sit vol</p><div class="price">$25<small>/Per Night</small></div><div class="pill pill-line">View More</div></div>
  <div class="abs room" style="left:905px"><div class="room-photo" role="img" aria-label="Villa living room with sofas"></div><span class="room-size">35 sq.m</span><h5>Villa</h5><p class="sans">Sed ut perspiciatis unde om natus error sit vol</p><div class="price">$25<small>/Per Night</small></div><div class="pill pill-line">View More</div></div>
</section>

<footer class="site-footer">
  <div class="abs foot-links">Contact &nbsp;/&nbsp; Prices &nbsp;/&nbsp; Awards &nbsp;/&nbsp; Company details &nbsp;/<br>Hotel Fact Sheet &nbsp;/&nbsp; Brochure &nbsp;/&nbsp; 360® VR &nbsp;/<br>Stay Safe Organizer &nbsp;/&nbsp; FAQ</div>
  <div class="abs foot-sep"></div>
  <div class="abs foot-legal">Terms &nbsp;&nbsp;/&nbsp;&nbsp; Disclaimer &nbsp;&nbsp;/&nbsp;&nbsp; Privacy Policy<br><span class="copy">&nbsp;&nbsp;&nbsp;&nbsp;© Copyrights 2021.All Rights Reserved.</span></div>
</footer>

</body>
</html>
```